Wavelume artwork for new single release

I need Wavelume artwork creating to release a new single on there.

The specs are:

Ideal size: 3000 x 3000 pixels
Minimum size: 1400 x 1400 pixels
Aspect ratio: 1:1 (must be a perfect square)
File format: JPG or PNG
Color space: sRGB
File size: Max 4MB

The song is called "Still, Can We Wander?"
The artist is "Milo Fenwright"

We have no images of Milo, so it really is open to imagination.

Target Market(s)

Wavelume listeners

Industry/Entity Type

Music

```html
<!DOCTYPE html>
<html lang="en">
<head>
<meta charset="utf-8">
<title>Still, Can We Wander? — Milo Fenwright</title>
<link href="https://fonts.googleapis.com/css2?family=Figtree:wght@400;700&display=swap" rel="stylesheet">
<style>
  :root {
    --ink: #000000;
    --paper: #ffffff;
  }
  html, body {
    margin: 0;
    padding: 0;
    width: 1200px;
    height: 1200px;
    overflow: hidden;
    background: var(--ink);
  }
  .cover {
    display: block;
    width: 1200px;
    height: 1200px;
  }
  .cover-frame {
    fill: none;
    stroke: var(--paper);
    stroke-width: 14;
  }
  .title-line {
    font-family: "Figtree", "Helvetica Neue", Arial, sans-serif;
    font-weight: 700;
    fill: var(--paper);
    letter-spacing: -0.02em;
  }
  .title-line--lead { font-size: 172px; }
  .title-line--hero { font-size: 290px; }
  .title-line--close { font-size: 206px; }
  .artist-name {
    font-family: "Figtree", "Helvetica Neue", Arial, sans-serif;
    font-weight: 400;
    font-size: 62px;
    fill: var(--paper);
    letter-spacing: 0.01em;
  }
</style>
</head>
<body>
  <svg class="cover" viewBox="0 0 1200 1200" xmlns="http://www.w3.org/2000/svg" role="img" aria-label="Still, Can We Wander? by Milo Fenwright">
    <rect class="cover-frame" x="68" y="68" width="1064" height="1064"/>
    <text class="title-line title-line--lead" x="600" y="426" text-anchor="middle">Still, Can</text>
    <text class="title-line title-line--hero" x="600" y="700" text-anchor="middle">We</text>
    <text class="title-line title-line--close" x="600" y="908" text-anchor="middle">Wander?</text>
    <text class="artist-name" x="600" y="1067" text-anchor="middle">MILO FENWRIGHT</text>
  </svg>
</body>
</html>
```